Updated VOLA Brochure for cultural event

We are seeking an updated brochure in a standard 8.5 by 11 size, and we have provided the current brochure and necessary information for inclusion. We desire a fresh new design that conveys a modern and elegant aesthetic. As we anticipate making changes to the brochure periodically, we require an editable program for its creation. Our First Nation Community values our beliefs and appearance, and we hope the brochure will reflect our welcoming nature while standing out from the crowd.
Attached Brochure is from last year
Wants and needs:
Page one. A redesign All the info on the page needs to be there but it needs a face lift.
Page two. Information is attached for that but do need this page editable for future. Join us for an immersive cultural experience at Pelham Creek First Nation (PCFN) community, located in Northeastern BC. We invite you to participate in the Vola Camping Experience, a unique opportunity to forge relationships with our community, connect with our Chief and Council, and engage with industry leaders. Your participation in this grassroots event will earn your company credibility for the work it performs in PCFN territory.

Through this experience, you'll gain an appreciation and understanding of our community and cultural values, while meeting with key office staff, industry C-Suite level executives, industry Indigenous relations staff, and local, regional, and provincial representatives in a positive and welcoming space. The recent Tarrow V. Ontario 2021 decision has significantly shifted how consultation and engagement will be managed on our lands. To help you better understand why managing cumulative effects is essential to PCFN, we welcome you to join us for a three-day camping experience from May 23 to May 26, 2023.

The Vola Camping Experience offers a variety of activities, including a dinner visit to NAH 'B'ilo, the 12,500-year-old cave, where an archeological dig is currently underway, accompanied by our economic development corporation team from Raska Development LP. The event also includes traditional bush camping in elegant teepees/wall tents, dry meat making, and participation in our Pelham Day, a 30+ year cultural education and anti-racism event held on May 25, 2023. During Pelham Day, over 400+ students from School District #47 participate in traditional activities, including moose hide preparation, beaver skinning, archaeology dig, dry-meat making, trapping demonstrations, Bannock on a stick, storytelling, drumming, and tea dance around the campfire to the beat of our drums.

Root yourself to the land, connect with your inner self, and be transformed alongside other important dignitaries as you partake in these multi-sensory experiences on our cultural grounds. This is our second combined camping/Pelham Day experience, and we hope to continue and build on it for future cultural tourism activities such as guided bush camps, hikes, and hunts.

If you are unable to join us for the full three-day camping experience, we encourage you to join us for the one-day Pelham Day event, along with other important decision-makers and political leaders. We have a helicopter landing area close to the activities for your convenience. Please RSVP to Owen March, Miyo? B'ilo Cultural Productions Manager at OwenMarch@pelhamcrk.example or Wendel Fusk, PCFN Councilor at Wfusk@pelhamcrk.example. We are looking forward to hosting you!

Page 3 - Signatures Names can be put in but I will need to add signatures after.
Page 4. 2023 Sponsors this will need to be editable as we get new ones in.
Page 5. Participant supplies check list. All of this is good just need to make it look better
Page 6. Agenda Dates need to change May 23-26 2023 This page also needs to be editable .. the days Dates need to change also.
Page 7 . Same info can be there.
All pages can use different photos where you need them..
Different logos on the sponsor page so that needs to be editable.
Daily Agenda needs to be editable .. definitely a better table

Things that need to be editable are dates (May 23-26th 2023)

I am just gathering some more photos for the brochure and will add them as I go .

Target Market(s)

Corporate partners

Colors
0054AA
0677BA
7BADD7
CADEEF
E8F1F8
0094D4
00A9DD
6FCCEA
C7EBF8
E9F6FB
00AB8E
00BBA5
67D7C9
C6EFE9
E9F9F6
59FF00
82FF00
B8FF75
E3FFCB
F4FFEA
FFF300
FFF600
FEFA6F
FFFEC7
FFFEE8
FFC000
F8CF3A
FAE287
FDF2CF
FEFAEE
F0912C
F2A743
F7CA91
FBE8D2
FDF5EE
EE7325
F08F49
F5BC92
FAE3D3
FDF4ED
EB3D1F
EC4F4E
F09395
F8D3D4
FCEDEE

Requirements
Must have
• The information that was provided
Nice to have
• We would like this to be very inviting and professional
Should not have
• cartoons or anything that looks cheap

```html
<!DOCTYPE html>
<html lang="en">
<head>
<meta charset="utf-8">
<title>Vola Executive Camping Experience 2023 – Brochure</title>
<link href="https://fonts.googleapis.com/css2?family=Montserrat:wght@400;600;700;800&family=Oswald:wght@500;600&family=Great+Vibes&display=swap" rel="stylesheet">
<style>
:root{
  --canvas:#a9a4a9;
  --ink:#0d0d0f;
  --night:#14161c;
  --paper:#ffffff;
  --yellow:#fff300;
  --gold:#ffc000;
  --blue-deep:#0054aa;
  --blue:#0094d4;
  --blue-soft:#7badd7;
  --blue-pale:#cadeef;
  --blue-mist:#e8f1f8;
  --teal:#00ab8e;
  --grey:#4a4d55;
  --text-light:#e9e9ec;
}
*{box-sizing:border-box;margin:0;padding:0}
html,body{width:1200px;height:2392px;overflow:hidden;background:var(--canvas)}
body{position:relative;font-family:"Montserrat",sans-serif;color:var(--ink)}
.spread{position:absolute;left:80px;width:1040px;overflow:hidden;box-shadow:0 4px 14px rgba(0,0,0,.35)}
.abs{position:absolute}
.photo{position:absolute}
.script{font-family:"Great Vibes",cursive;font-weight:400}
.brand{font-family:"Montserrat",sans-serif;font-weight:700;display:flex;align-items:center;gap:8px}
.brand .dot{width:12px;height:12px;border-radius:50%;background:var(--yellow);display:inline-block}

/* cover */
.cover{top:32px;height:560px;background:var(--ink)}
.cover .hero{left:0;top:0;width:640px;height:560px;clip-path:polygon(0 0,100% 0,82% 100%,0 100%);
  background:radial-gradient(circle at 45% 55%,#f5d36b 0,#d97a2a 14%,#7a2f7a 32%,#1c4a8a 52%,#0b0d18 80%)}
.cover .brand{left:690px;top:70px;color:var(--paper);font-size:64px;letter-spacing:1px}
.cover .brand-sub{left:694px;top:150px;color:var(--paper);font-size:13px;letter-spacing:6px;font-weight:600}
.cover .band{left:600px;top:200px;width:440px;height:70px;background:var(--yellow);
  clip-path:polygon(6% 0,100% 0,100% 100%,0 100%);display:flex;align-items:center;justify-content:space-between;padding:0 24px 0 56px}
.cover .band span{font-weight:800;font-size:15px;line-height:1.2;color:var(--ink);text-transform:uppercase}
.cover .band b{font-family:"Oswald",sans-serif;font-size:40px;color:var(--ink)}
.cover .nation{left:760px;top:310px;display:flex;align-items:center;gap:12px;color:var(--paper);font-size:13px;font-weight:600}
.cover .nation i{width:54px;height:54px;border-radius:50%;background:var(--grey);display:block}
.cover .stripes{left:0;top:0}

/* info spread */
.info{top:616px;height:432px;background:var(--night);color:var(--text-light)}
.col{position:absolute;top:0;height:432px;width:260px}
.info .moon{left:0;top:0;width:260px;height:170px;background:radial-gradient(circle at 70% 30%,#e6e9f0 0,#8a93a8 8%,#1e2740 30%,#07090f 75%)}
.info .c1 .brand{position:absolute;left:22px;top:176px;color:var(--paper);font-size:30px}
.info .headline{position:absolute;left:22px;top:222px;width:220px;font-family:"Oswald",sans-serif;font-weight:600;
  color:var(--yellow);font-size:19px;line-height:1.15;text-transform:uppercase}
.info .path{left:260px;top:0;width:260px;height:150px;background:linear-gradient(160deg,#1a2230,#6b4b2a 55%,#f0a24a 75%,#20160f)}
.info .tent{left:520px;top:230px;width:260px;height:202px;background:radial-gradient(circle at 50% 45%,#ffd37a 0,#c9782e 18%,#3a2a22 45%,#0c0d12 80%)}
.body-text{position:absolute;font-size:7.1px;line-height:10.2px;color:var(--text-light)}
.body-text p+p{margin-top:5px}
.body-text b{color:var(--yellow);font-weight:600}
.info .t2{left:278px;top:162px;width:226px}
.info .t3{left:536px;top:18px;width:228px}
.info .t4{left:796px;top:40px;width:226px}
.info .hosting{left:560px;top:372px;font-size:30px;color:var(--paper)}

/* signatures & sponsors */
.partners{top:1072px;height:448px;background:var(--paper)}
.partners .feather{left:0;top:0;width:170px;height:448px;clip-path:polygon(0 0,100% 0,55% 100%,0 100%);
  background:linear-gradient(160deg,#2b6fb0,#6fccea 35%,#f0912c 65%,#eb3d1f)}
.partners .title{font-size:44px;color:var(--ink)}
.sig-title{left:250px;top:26px}
.sig-list{left:240px;top:110px;width:240px}
.sig-row{height:74px;border-bottom:1px solid #b9bcc4;position:relative}
.sig-row span{position:absolute;left:0;top:6px;font-size:8px;font-weight:600;color:#444}
.spon-title{left:640px;top:26px}
.spon-grid{left:570px;top:110px;width:300px;display:grid;grid-template-columns:1fr 1fr;gap:18px 16px}
.sponsor{display:flex;align-items:center;gap:7px;font-weight:700;font-size:13px;color:var(--grey)}
.sponsor i{width:14px;height:14px;background:var(--blue-soft);display:block}
.partners .tool{left:890px;top:0;width:150px;height:448px;background:linear-gradient(180deg,#dfe3e6,#9b7a52 40%,#c8733a 60%,#e9ecee)}

/* checklist & agenda */
.plans{top:1544px;height:472px;background:var(--paper)}
.check-head{left:0;top:0;width:520px;height:92px;background:var(--ink);color:var(--paper)}
.check-head .brand{position:absolute;left:18px;top:26px;font-size:24px}
.check-head h2{position:absolute;left:150px;top:18px;font-size:19px;font-weight:800;letter-spacing:1px}
.check-head .script{position:absolute;left:230px;top:34px;font-size:40px;color:var(--yellow)}
.check-table{position:absolute;left:24px;top:108px;width:472px;border-collapse:collapse;font-size:7.5px}
.check-table th{background:var(--grey);color:var(--paper);text-align:left;padding:4px 5px;font-weight:700}
.check-table td{border:1px solid #c9ccd2;padding:3.2px 5px;height:15px}
.check-table td.box{width:24px}
.check-foot{left:0;top:430px;width:520px;height:42px;background:var(--ink);color:var(--paper);font-size:7px;line-height:11px;padding:8px 24px}
.check-foot b{color:var(--yellow)}
.agenda-page{left:520px;top:0;width:520px;height:472px;background:var(--blue-mist)}
.agenda-card{left:560px;top:30px;width:360px;height:418px;background:var(--paper);transform:rotate(-2deg);box-shadow:0 2px 8px rgba(0,0,0,.18);padding:18px 20px}
.agenda-card h2{font-size:40px;text-align:center;color:var(--blue-deep)}
.agenda-card h3{font-size:8px;font-weight:700;text-align:center;letter-spacing:1px;margin:2px 0 8px}
.agenda{width:100%;border-collapse:collapse;font-size:7px}
.agenda th{background:var(--blue-deep);color:var(--paper);padding:4px;text-align:left}
.agenda td{border-bottom:1px solid var(--blue-pale);padding:4px;vertical-align:top;line-height:9px}
.agenda td:first-child{font-weight:700;width:64px;color:var(--blue-deep)}
.thumb{position:absolute;left:944px;width:84px;height:78px;border:3px solid var(--paper)}

/* back */
.back{position:absolute;left:320px;top:2040px;width:560px;height:320px;background:var(--ink);box-shadow:0 4px 14px rgba(0,0,0,.35);overflow:hidden}
.back .crowd{left:0;top:0;width:560px;height:200px;background:linear-gradient(180deg,#6f8fb0,#5d6b4a 50%,#3e3a30)}
.back .thanks{left:0;top:212px;width:560px;text-align:center;color:var(--paper)}
.back .thanks small{display:block;font-size:8px;letter-spacing:2px;color:#aaa}
.back .thanks strong{display:block;font-size:14px;font-weight:700;margin-top:4px}
.back .thanks .script{font-size:34px;color:var(--yellow);line-height:1}
.back .brand{left:230px;top:286px;color:var(--paper);font-size:18px}
</style>
</head>
<body>

<!-- Cover -->
<section class="spread cover">
  <div class="photo hero" role="img" aria-label="Photo of a glowing wall tent at night under colourful lights"></div>
  <svg class="abs stripes" width="1040" height="560" viewBox="0 0 1040 560">
    <polygon points="520,560 600,380 640,380 560,560" fill="#2c2f36"/>
    <line x1="0" y1="520" x2="300" y2="560" stroke="#ffffff" stroke-width="2"/>
    <line x1="600" y1="380" x2="1040" y2="380" stroke="#ffffff" stroke-width="1"/>
    <polygon points="1040,430 1040,560 820,560" fill="#2c2f36"/>
  </svg>
  <div class="abs brand">Vola <span class="dot"></span></div>
  <div class="abs brand-sub">EXPERIENCE</div>
  <div class="abs band"><span>Vola Executive<br>Camping Experience</span><b>2023</b></div>
  <div class="abs nation"><i></i>Pelham Creek First Nation</div>
</section>

<!-- Information -->
<section class="spread info">
  <div class="col c1">
    <div class="photo moon" role="img" aria-label="Photo of a full moon over a dark landscape"></div>
    <div class="brand">Vola <span class="dot"></span></div>
    <div class="headline">Join us for an immersive cultural experience at Pelham Creek First Nation (PCFN) community, located in Northeastern BC.</div>
  </div>
  <div class="photo path" role="img" aria-label="Photo of a lantern-lit path through the woods at dusk"></div>
  <div class="body-text t2">
    <p>We invite you to participate in the Vola Camping Experience, a unique opportunity to forge relationships with our community, connect with our Chief and Council, and engage with industry leaders. Your participation in this grassroots event will earn your company credibility for the work it performs in PCFN territory.</p>
    <p>Through this experience, you'll gain an appreciation and understanding of our community and cultural values, while meeting with key office staff, industry C-Suite level executives, industry Indigenous relations staff, and local, regional, and provincial representatives in a positive and welcoming space. The recent Tarrow V. Ontario 2021 decision has significantly shifted how consultation and engagement will be managed on our lands. To help you better understand why managing cumulative effects is essential to PCFN, we welcome you to join us for a three-day camping experience from <b>May 23 to May 26, 2023.</b></p>
  </div>
  <div class="body-text t3">
    <p>The Vola Camping Experience offers a variety of activities, including a dinner visit to NAH 'B'ilo, the 12,500-year-old cave, where an archeological dig is currently underway, accompanied by our economic development corporation team from Raska Development LP. The event also includes traditional bush camping in elegant teepees/wall tents, dry meat making, and participation in our Pelham Day, a 30+ year cultural education and anti-racism event held on May 25, 2023.</p>
    <p>During Pelham Day, over 400+ students from School District #47 participate in traditional activities, including moose hide preparation, beaver skinning, archaeology dig, dry-meat making, trapping demonstrations, Bannock on a stick, storytelling, drumming, and tea dance around the campfire to the beat of our drums.</p>
  </div>
  <div class="photo tent" role="img" aria-label="Photo of a lit tent and campfire at night"></div>
  <div class="abs script hosting">We are looking forward to hosting you!</div>
  <div class="body-text t4">
    <p>Root yourself to the land, connect with your inner self, and be transformed alongside other important dignitaries as you partake in these multi-sensory experiences on our cultural grounds. This is our second combined camping/Pelham Day experience, and we hope to continue and build on it for future cultural tourism activities such as guided bush camps, hikes, and hunts.</p>
    <p><b>If you are unable to join us for the full three-day camping experience, we encourage you to join us for the one-day Pelham Day event,</b> along with other important decision-makers and political leaders. We have a helicopter landing area close to the activities for your convenience.</p>
    <p>Please RSVP to Owen March, Miyo? B'ilo Cultural Productions Manager at OwenMarch@pelhamcrk.example or Wendel Fusk, PCFN Councilor at Wfusk@pelhamcrk.example.</p>
    <p><b>We are looking forward to hosting you!</b></p>
  </div>
</section>

<!-- Signatures & Sponsors -->
<section class="spread partners">
  <div class="photo feather" role="img" aria-label="Illustration of a colourful beaded feather"></div>
  <svg class="abs" style="left:0;top:0" width="1040" height="448" viewBox="0 0 1040 448">
    <polygon points="170,0 260,0 190,90" fill="#e8f1f8"/>
    <polygon points="520,448 600,448 520,360" fill="#cadeef"/>
    <polygon points="840,0 890,0 890,120" fill="#7badd7"/>
    <polygon points="860,448 890,448 890,330" fill="#cadeef"/>
    <line x1="520" y1="30" x2="520" y2="420" stroke="#dde1e6" stroke-width="1"/>
  </svg>
  <div class="abs title script sig-title">Signatures</div>
  <div class="abs sig-list">
    <div class="sig-row"><span>Chief – Pelham Creek First Nation</span></div>
    <div class="sig-row"><span>Councilor – Pelham Creek First Nation</span></div>
    <div class="sig-row"><span>Manager – Miyo? B'ilo Cultural Productions</span></div>
    <div class="sig-row"><span>Director – Raska Development LP</span></div>
  </div>
  <div class="abs title script spon-title">Sponsors</div>
  <div class="abs spon-grid">
    <div class="sponsor"><i></i>Corvan 360</div>
    <div class="sponsor"><i></i>Trellis Energy</div>
    <div class="sponsor"><i></i>Petrova</div>
    <div class="sponsor"><i></i>Terramark</div>
    <div class="sponsor"><i></i>Ovello</div>
    <div class="sponsor"><i></i>Fractal Power</div>
    <div class="sponsor"><i></i>Raska Development LP</div>
    <div class="sponsor"><i></i>Pelham Creek</div>
  </div>
  <div class="photo tool" role="img" aria-label="Photo of a beaded traditional tool hanging outdoors"></div>
</section>

<!-- Checklist & Agenda -->
<section class="spread plans">
  <div class="abs check-head">
    <div class="brand">Vola <span class="dot"></span></div>
    <h2>PARTICIPANT SUPPLIES</h2>
    <div class="script">Check list</div>
  </div>
  <table class="check-table">
    <tr><th>Supplies</th><th>Qty</th><th>✓</th><th>Notes</th></tr>
    <tr><td>Sleeping bag rated for cool nights</td><td class="box">1</td><td class="box"></td><td>Nights drop near zero</td></tr>
    <tr><td>Pillow and camp blanket</td><td class="box">1</td><td class="box"></td><td></td></tr>
    <tr><td>Warm jacket and rain gear</td><td class="box">1</td><td class="box"></td><td>Weather can change fast</td></tr>
    <tr><td>Sturdy boots for walking</td><td class="box">1</td><td class="box"></td><td></td></tr>
    <tr><td>Toque, gloves and wool socks</td><td class="box">2</td><td class="box"></td><td></td></tr>
    <tr><td>Flashlight or headlamp</td><td class="box">1</td><td class="box"></td><td>Spare batteries</td></tr>
    <tr><td>Bug spray and sunscreen</td><td class="box">1</td><td class="box"></td><td></td></tr>
    <tr><td>Toiletries and towel</td><td class="box">1</td><td class="box"></td><td></td></tr>
    <tr><td>Personal medication</td><td class="box">–</td><td class="box"></td><td>Tell staff on arrival</td></tr>
    <tr><td>Reusable water bottle and mug</td><td class="box">1</td><td class="box"></td><td></td></tr>
    <tr><td>Camp chair</td><td class="box">1</td><td class="box"></td><td>Optional</td></tr>
    <tr><td>Phone charger / power bank</td><td class="box">1</td><td class="box"></td><td>Limited power on site</td></tr>
    <tr><td>Change of clothes for each day</td><td class="box">3</td><td class="box"></td><td></td></tr>
    <tr><td>Small gift for the host family</td><td class="box">1</td><td class="box"></td><td>Optional</td></tr>
    <tr><td>Cash for local crafts</td><td class="box">–</td><td class="box"></td><td></td></tr>
    <tr><td>Notebook and pen</td><td class="box">1</td><td class="box"></td><td></td></tr>
    <tr><td>Daypack</td><td class="box">1</td><td class="box"></td><td></td></tr>
  </table>
  <div class="abs check-foot"><b>Please note:</b> meals, tents, cots and firewood are provided for all guests.<br>Questions? Contact OwenMarch@pelhamcrk.example or Wfusk@pelhamcrk.example</div>

  <div class="abs agenda-page"></div>
  <svg class="abs" style="left:520px;top:0" width="520" height="472" viewBox="0 0 520 472">
    <polygon points="0,0 120,0 0,140" fill="#7badd7"/>
    <polygon points="0,472 0,360 140,472" fill="#0094d4"/>
  </svg>
  <div class="abs agenda-card">
    <h2 class="script">Agenda Dates</h2>
    <h3>VOLA IMMERSIVE EXECUTIVE EXPERIENCE · MAY 23–26, 2023</h3>
    <table class="agenda">
      <tr><th>Date</th><th>Activities</th></tr>
      <tr><td>Tue, May 23</td><td>Guest arrival and check-in at camp<br>Welcome from Chief and Council<br>Settle into teepees and wall tents<br>Evening meal and fireside stories</td></tr>
      <tr><td>Wed, May 24</td><td>Breakfast at the cook shack<br>Dry meat making and land walk<br>Meetings with key office staff<br>Dinner visit to NAH 'B'ilo cave with Raska Development LP</td></tr>
      <tr><td>Thu, May 25</td><td>Pelham Day with School District #47<br>Hide preparation, trapping and dig demos<br>Bannock on a stick and drumming<br>Tea dance around the campfire</td></tr>
      <tr><td>Fri, May 26</td><td>Closing breakfast and talking circle<br>Camp breakdown and farewells<br>Departures</td></tr>
    </table>
  </div>
  <div class="photo thumb" style="top:22px;background:linear-gradient(160deg,#7ea7c9,#4f6b3a)" role="img" aria-label="Photo of camp tents in a meadow"></div>
  <div class="photo thumb" style="top:110px;background:linear-gradient(160deg,#c9a07a,#5a3b26)" role="img" aria-label="Photo of dry meat on a rack"></div>
  <div class="photo thumb" style="top:198px;background:linear-gradient(160deg,#e8b05a,#3a2415)" role="img" aria-label="Photo of a campfire gathering"></div>
  <div class="photo thumb" style="top:286px;background:linear-gradient(160deg,#8fb6d9,#6b7d5a)" role="img" aria-label="Photo of the cultural grounds"></div>
  <div class="photo thumb" style="top:374px;background:linear-gradient(160deg,#9ac0a0,#2f4a3a)" role="img" aria-label="Photo of a forest trail"></div>
</section>

<!-- Back page -->
<section class="back">
  <div class="photo crowd" role="img" aria-label="Photo of students gathered outdoors at Pelham Day"></div>
  <div class="abs thanks">
    <small>SEE YOU AT THE VOLA CAMPING EXPERIENCE</small>
    <strong>Wasja sesrala</strong>
    <span class="script">Thank You!</span>
  </div>
  <div class="abs brand">Vola <span class="dot"></span></div>
</section>

</body>
</html>
```